brovalo business card

We are a commercial cleaning/janitorial service company our main target is building owners and managers.
Would like to see the icon as a background shadow in the front and the full logo in white on the back with a blue background.  On the card:
Dorn Huxley, Operations Manager, dorn@brovalo.example
47315-K Pike Rd. 81 #452
Granger, IN 46599
574.555.0148, 888.555.0172

Updates
please include cell 574.555.0163
                                   
Thank you
If possible the fading logo on the front should be very subtle and light and lets look at centering that as well
thanks

```html
<!DOCTYPE html>
<html lang="en">
<head>
<meta charset="utf-8">
<title>brovalo business card</title>
<link rel="stylesheet" href="https://fonts.googleapis.com/css2?family=Source+Sans+3:ital,wght@0,400;0,700;1,700&display=swap">
<style>
  :root {
    --brand-blue: #0a72b9;
    --brand-charcoal: #3a3a3c;
    --ink: #333333;
    --card: #ffffff;
    --watermark: rgba(10, 114, 185, 0.05);
    --backdrop: #e6e6e6;
  }
  html, body {
    margin: 0;
    padding: 0;
    width: 960px;
    height: 1200px;
    overflow: hidden;
    background: var(--backdrop);
    font-family: "Source Sans 3", Arial, sans-serif;
  }
  .canvas {
    position: relative;
    width: 960px;
    height: 1200px;
  }
  .card {
    position: absolute;
    background: var(--card);
    border-radius: 28px;
    overflow: hidden;
    box-shadow: 0 4px 10px rgba(0,0,0,0.25);
  }
  .card-front { left: 60px; top: 100px; width: 840px; height: 480px; }
  .card-back  { left: 55px; top: 640px; width: 840px; height: 480px; background: var(--brand-blue); }

  .watermark {
    position: absolute;
    left: 270px;
    top: 90px;
    width: 300px;
    height: 300px;
    border-radius: 50%;
    background: var(--watermark);
  }

  .brand {
    position: absolute;
    display: flex;
    align-items: center;
    left: 0; right: 0;
    justify-content: center;
  }
  .brand-dot {
    border-radius: 50%;
    background: var(--brand-charcoal);
    flex: none;
  }
  .brand-name {
    color: var(--brand-blue);
    font-weight: 700;
    line-height: 1;
    letter-spacing: -1px;
  }
  .card-front .brand { top: 70px; gap: 34px; }
  .card-front .brand-dot { width: 134px; height: 134px; }
  .card-front .brand-name { font-size: 76px; }

  .card-back .brand { top: 143px; gap: 44px; }
  .card-back .brand-dot { width: 185px; height: 185px; background: #ffffff; }
  .card-back .brand-name { font-size: 118px; color: #ffffff; }

  .contact {
    position: absolute;
    left: 0; right: 0;
    top: 272px;
    text-align: center;
    color: var(--ink);
    font-size: 23px;
    line-height: 34px;
  }
  .contact p { margin: 0; }
  .contact .address { margin-top: 5px; }
  .contact .label { font-weight: 700; font-style: italic; }
  .contact .sep { margin: 0 8px; }

  .swoosh {
    position: absolute;
    left: 0; top: 0;
    width: 840px; height: 480px;
  }
  .swoosh .rule { fill: var(--brand-charcoal); }
  .swoosh .band { fill: var(--brand-blue); }

  .person {
    position: absolute;
    left: 0; right: 0;
    top: 431px;
    margin: 0;
    text-align: center;
    color: #ffffff;
    font-size: 20px;
    line-height: 30px;
  }
  .person .person-name { font-weight: 700; font-size: 23px; }
</style>
</head>
<body>
<main class="canvas">

  <section class="card card-front" aria-label="Card front">
    <span class="watermark" aria-hidden="true"></span>

    <div class="brand">
      <span class="brand-dot"></span>
      <span class="brand-name">brovalo</span>
    </div>

    <div class="contact">
      <p><span class="label">p</span> : 574.555.0148<span class="sep">|</span>888.555.0172<span class="sep">|</span><span class="label">c</span> : 574.555.0163</p>
      <p><span class="label">e</span> : dorn@brovalo.example<span class="sep">|</span><span class="label">w</span> : www.brovalo.example</p>
      <p class="address">47315-K Pike Rd. 81 #452, Granger, IN 46599</p>
    </div>

    <svg class="swoosh" viewBox="0 0 840 480" aria-hidden="true">
      <path class="rule" d="M0,414 Q420,372 840,414 L840,424 Q420,384 0,424 Z"/>
      <path class="band" d="M0,430 Q420,392 840,430 L840,480 L0,480 Z"/>
    </svg>

    <p class="person"><span class="person-name">DORN HUXLEY,</span> Operations Manager</p>
  </section>

  <section class="card card-back" aria-label="Card back">
    <div class="brand">
      <span class="brand-dot"></span>
      <span class="brand-name">brovalo</span>
    </div>
  </section>

</main>
</body>
</html>
```